Growth-Bridge: Plus - EU-funded management consulting

A website to inform possible customers about my management consulting services for small and medium sized companies. I am using a funding for small and medium companies to do 10 days of workshops and coaching about leadership, further education and employee's health. The Funding is called "Wachstumsbrücke Plus" which means something like: Humans are the value of the company. The official logo is attached as a

Target Market(s)

Small and medium sized companies that want to improve their employee's well being and efficiency.

Industry/Entity Type

Management Consulting

Contact Information for Business Card

Veit Brosche, Kastanienweg 14, 10437 Berlin

Logo Text

WachstumsBrücke Plus - Beratung

Font styles to use
Serif
Sans Serif

Requirements
Must have
• a friendly and professional design
Nice to have
• saying somthing about: employees, leadership, further education and employees health are important to us.
Should not have
• should not be too shimmering

```html
<!DOCTYPE html>
<html lang="en">
<head>
<meta charset="utf-8">
<title>Wachstumsbrücke Plus – Management Consulting</title>
<link href="https://fonts.googleapis.com/css2?family=Open+Sans:wght@400;600;700;800&display=swap" rel="stylesheet">
<style>
:root{
  --blue:#2a8fd6;
  --blue-dark:#1f74b3;
  --ink:#3a3a3a;
  --muted:#6d6d6d;
  --light:#f4f4f4;
  --band:#ececec;
  --line:#dcdcdc;
  --footer:#323232;
  --footer-text:#bdbdbd;
  --social:#d9443a;
  --white:#ffffff;
}
*{box-sizing:border-box;margin:0;padding:0}
html,body{width:781px;height:1200px;overflow:hidden}
body{font-family:"Open Sans",Arial,sans-serif;color:var(--ink);background:var(--white);font-size:8px;line-height:1.45}
.page{position:relative;width:781px;height:1200px}

/* header */
.site-header{height:52px;display:flex;align-items:center;justify-content:space-between;padding:0 45px}
.brand{display:flex;align-items:center;gap:7px;font-weight:700;font-size:14px;color:var(--blue)}
.brand-mark{width:14px;height:14px;background:var(--blue)}
.contact-block{display:flex;align-items:center;gap:10px}
.icon-circle{width:24px;height:24px;border-radius:50%;background:var(--blue);display:flex;align-items:center;justify-content:center}
.contact-lines{text-align:right}
.contact-email{font-size:8px;color:var(--muted)}
.contact-phone{font-size:18px;font-weight:600;color:var(--ink);line-height:1.1}
.social-row{display:flex;gap:3px;margin-top:2px;justify-content:flex-end}
.social-square{width:10px;height:10px;background:var(--social)}

/* nav */
.main-nav{height:42px;background:linear-gradient(#f7f7f7,#e6e6e6);border-top:1px solid var(--line);border-bottom:1px solid var(--line);padding:0 45px;display:flex;align-items:flex-end}
.main-nav a{display:block;width:68px;height:30px;line-height:30px;text-align:center;color:var(--muted);text-decoration:none;font-size:8px;border-right:1px solid var(--line)}
.main-nav a.is-active{background:var(--blue);color:var(--white);font-weight:600}

/* hero */
.hero{position:relative;height:322px}
.hero-photo{position:absolute;inset:0;background:linear-gradient(100deg,#5f6d79 0%,#8c98a3 30%,#c6ced5 55%,#7e8c99 78%,#4d5b68 100%)}
.hero-copy{position:absolute;left:45px;top:56px;width:330px;color:var(--white)}
.hero-title{font-weight:600;font-size:21px;line-height:1.15;letter-spacing:.3px}
.hero-title strong{display:block;font-size:32px;font-weight:800}
.hero-text{margin-top:12px;font-size:8px;line-height:1.6;opacity:.92}
.btn{display:inline-block;background:var(--blue);color:var(--white);font-size:8px;font-weight:600;text-decoration:none;border-radius:2px}
.hero .btn{margin-top:16px;padding:8px 16px}
.hero-dots{position:absolute;bottom:18px;left:0;right:0;display:flex;justify-content:center;gap:6px}
.hero-dots span{width:6px;height:6px;border-radius:50%;border:1px solid var(--white)}
.hero-dots span.is-current{background:var(--white)}

/* services */
.services{height:414px;padding-top:36px}
.section-heading{text-align:center;font-size:19px;font-weight:600;line-height:1.25;color:var(--ink)}
.service-grid{display:flex;justify-content:space-between;padding:0 45px;margin-top:34px}
.service-card{width:208px}
.service-title{font-size:12.5px;font-weight:700;color:var(--blue);margin-bottom:10px}
.service-photo{height:98px;background:linear-gradient(135deg,#9fb3c4,#d9dde1 55%,#b59e86)}
.service-lead{margin-top:12px;font-weight:700;font-size:8px}
.service-text{font-size:7.5px;color:var(--muted);margin-top:2px}
.service-card .btn{margin-top:12px;padding:6px 13px}

/* band */
.info-band{height:242px;background:var(--band);display:flex;padding:24px 45px 0;gap:26px}
.band-title{font-size:17px;font-weight:800;color:var(--blue-dark);margin-bottom:12px}
.why-us{width:160px}
.why-list{list-style:none}
.why-list li{font-size:7px;font-weight:600;padding:3px 0;display:flex;align-items:center;gap:6px}
.why-list li::before{content:"";width:4px;height:4px;background:var(--blue)}
.mission{width:290px}
.mission-body{display:flex;gap:10px}
.mission-photo{width:140px;height:100px;flex:none;background:linear-gradient(135deg,#6b7f8f,#c9b79b 50%,#8fa3b2)}
.mission-text{font-size:7px;color:var(--muted)}
.mission-text .lead{color:var(--blue);margin-bottom:4px}
.read-more{display:block;margin-top:10px;font-size:7px;font-weight:700;color:var(--ink)}
.testimonials{width:190px}
.quote-box{background:var(--white);border:1px solid var(--line);padding:10px 12px;font-size:7px;color:var(--muted);position:relative}
.quote-mark{position:absolute;left:6px;top:4px;font-size:18px;color:var(--blue);font-weight:800;line-height:1}
.quote-box p{padding-left:12px}
.client{display:flex;align-items:center;gap:8px;margin-top:10px;justify-content:flex-end}
.client-photo{width:30px;height:30px;background:linear-gradient(#9a8a7a,#5d534b)}
.client-name{font-size:8px;font-weight:700}
.client-role{font-size:6.5px;color:var(--muted)}

/* footer */
.site-footer{position:absolute;left:0;right:0;bottom:0;height:128px;background:var(--footer);color:var(--footer-text)}
.footer-row{display:flex;align-items:center;padding:34px 45px 0;gap:16px}
.footer-item{display:flex;align-items:center;gap:9px;font-size:7.5px;width:200px}
.footer-icon{width:26px;height:26px;border-radius:50%;background:#444;display:flex;align-items:center;justify-content:center;flex:none}
.footer-social{display:flex;gap:6px;width:110px}
.footer-social span{width:10px;height:10px;border-radius:50%;background:#6b6b6b}
.newsletter{display:flex;width:140px;height:24px;margin-left:auto}
.newsletter-input{flex:1;background:#f0f0f0;font-size:7px;color:#999;padding:0 8px;line-height:24px}
.newsletter-send{width:26px;background:#555;display:flex;align-items:center;justify-content:center}
.copyright{position:absolute;bottom:10px;left:0;right:0;text-align:center;font-size:6.5px;color:#8a8a8a}
</style>
</head>
<body>
<div class="page">

  <header class="site-header">
    <div class="brand"><span class="brand-mark"></span>Wachstumsbrücke Plus</div>
    <div class="contact-block">
      <div class="icon-circle">
        <svg width="12" height="12" viewBox="0 0 24 24"><path fill="#fff" d="M6.6 10.8a15 15 0 0 0 6.6 6.6l2.2-2.2c.3-.3.7-.4 1-.2 1.1.4 2.3.6 3.6.6.6 0 1 .4 1 1V20c0 .6-.4 1-1 1A17 17 0 0 1 3 4c0-.6.4-1 1-1h3.5c.6 0 1 .4 1 1 0 1.3.2 2.5.6 3.6.1.3 0 .7-.2 1z"/></svg>
      </div>
      <div class="contact-lines">
        <div class="contact-email">info@wachstumsbruecke-plus.de</div>
        <div class="contact-phone">800-555-2468</div>
      </div>
      <div class="social-row" style="align-self:flex-end;margin-bottom:9px">
        <span class="social-square"></span><span class="social-square"></span><span class="social-square"></span>
      </div>
    </div>
  </header>

  <nav class="main-nav">
    <a href="#" class="is-active">Home</a>
    <a href="#">About</a>
    <a href="#">Services</a>
    <a href="#">Testimonials</a>
    <a href="#">Contact</a>
  </nav>

  <section class="hero">
    <div class="hero-photo" role="img" aria-label="Photo of two business consultants discussing documents in an office"></div>
    <div class="hero-copy">
      <h1 class="hero-title">A CLEAR TOMMOROW FOR <strong>YOUR BUSINESS !</strong></h1>
      <p class="hero-text">We support small and medium sized companies with workshops and coaching on leadership, further education and employee health, funded for ten days of consulting.</p>
      <a href="#" class="btn">Know More</a>
    </div>
    <div class="hero-dots"><span></span><span class="is-current"></span><span></span><span></span></div>
  </section>

  <section class="services">
    <h2 class="section-heading">We offer services to<br>small and medium sized companies</h2>
    <div class="service-grid">
      <article class="service-card">
        <h3 class="service-title">Leadership workshop</h3>
        <div class="service-photo" role="img" aria-label="Photo of a manager leading a team meeting"></div>
        <p class="service-lead">Leading teams with clarity and trust.</p>
        <p class="service-text">Practical sessions help managers set goals, give feedback and guide their people through change with confidence.</p>
        <a href="#" class="btn">Read More</a>
      </article>
      <article class="service-card">
        <h3 class="service-title">Employee health workshop</h3>
        <div class="service-photo" role="img" aria-label="Photo of colleagues in a group workshop"></div>
        <p class="service-lead">Healthy people, strong company.</p>
        <p class="service-text">We show how workload, breaks and good cooperation keep employees well, motivated and productive every day.</p>
        <a href="#" class="btn">Read More</a>
      </article>
      <article class="service-card">
        <h3 class="service-title">Further Educations</h3>
        <div class="service-photo" role="img" aria-label="Photo of employees learning together at a laptop"></div>
        <p class="service-lead">Skills that grow with your business.</p>
        <p class="service-text">Tailored training plans give your staff new knowledge and open real paths for development inside the company.</p>
        <a href="#" class="btn">Read More</a>
      </article>
    </div>
  </section>

  <section class="info-band">
    <div class="why-us">
      <h3 class="band-title">WHY CHOOSE US :</h3>
      <ul class="why-list">
        <li>RISK ASSESSMENT</li>
        <li>BUSINESS ANALYSIS</li>
        <li>PARTNERSHIP PROGRAM</li>
        <li>INTERACTIVE WAREHOUSE</li>
        <li>MARKET RESEARCH</li>
        <li>ADAPTIVE ENVIRONMENT</li>
      </ul>
    </div>
    <div class="mission">
      <h3 class="band-title">OUR MISSION :</h3>
      <div class="mission-body">
        <div class="mission-photo" role="img" aria-label="Photo of hands working together over a desk"></div>
        <div class="mission-text">
          <p class="lead">Employees, leadership, further education and employee health are important to us.</p>
          <p>We believe people are the true value of every company. Our consulting helps smaller firms build good leadership, keep their teams healthy and invest in learning that lasts.</p>
          <span class="read-more">READ MORE</span>
        </div>
      </div>
    </div>
    <div class="testimonials">
      <h3 class="band-title">TESTIMONIALS :</h3>
      <div class="quote-box">
        <span class="quote-mark">“</span>
        <p>The workshops changed how our managers lead. Our team feels heard, sick days went down and everyone is learning again.</p>
      </div>
      <div class="client">
        <div class="client-photo" role="img" aria-label="Portrait photo of the client"></div>
        <div><div class="client-name">Mark Lindner</div><div class="client-role">(CLIENT)</div></div>
      </div>
    </div>
  </section>

  <footer class="site-footer">
    <div class="footer-row">
      <div class="footer-item">
        <div class="footer-icon">
          <svg width="11" height="13" viewBox="0 0 24 28"><path fill="#ddd" d="M12 0a9 9 0 0 0-9 9c0 7 9 19 9 19s9-12 9-19a9 9 0 0 0-9-9zm0 12.5A3.5 3.5 0 1 1 12 5.5a3.5 3.5 0 0 1 0 7z"/></svg>
        </div>
        <div>Kastanienweg 14,<br>10437 Berlin</div>
      </div>
      <div class="footer-item">
        <div class="footer-icon">
          <svg width="11" height="11" viewBox="0 0 24 24"><path fill="#ddd" d="M6.6 10.8a15 15 0 0 0 6.6 6.6l2.2-2.2c.3-.3.7-.4 1-.2 1.1.4 2.3.6 3.6.6.6 0 1 .4 1 1V20c0 .6-.4 1-1 1A17 17 0 0 1 3 4c0-.6.4-1 1-1h3.5c.6 0 1 .4 1 1 0 1.3.2 2.5.6 3.6.1.3 0 .7-.2 1z"/></svg>
        </div>
        <div>Office: (030) 481 7260<br>Toll Free: 0800 555 3190</div>
      </div>
      <div class="footer-social"><span></span><span></span><span></span></div>
      <div class="newsletter">
        <div class="newsletter-input">Newsletter signup</div>
        <div class="newsletter-send">
          <svg width="11" height="11" viewBox="0 0 24 24"><path fill="#fff" d="M2 21l21-9L2 3v7l15 2-15 2z"/></svg>
        </div>
      </div>
    </div>
    <p class="copyright">Copyright © 2015 · All Rights Reserved</p>
  </footer>

</div>
</body>
</html>
```